Verrowdale Chamber of Commerce Website

We have been asked to design a new website for the Verrowdale Chamber of Commerce. The mission of the Greater Verrowdale Chamber of Commerce is to develop and promote an economically vibrant business community aggressively. The website should reflect a modern, professional design that showcases local businesses and promotes the programs the Chamber has to offer.

```html
<!DOCTYPE html>
<html lang="en">
<head>
<meta charset="utf-8">
<title>Greater Verrowdale Chamber of Commerce</title>
<link href="https://fonts.googleapis.com/css2?family=Poppins:wght@300;400;500;600;700&display=swap" rel="stylesheet">
<style>
:root{
  --brand:#3b6db5;
  --brand-dark:#1f3f7a;
  --royal:#1f49c4;
  --navy:#23364f;
  --ink:#1d1d1d;
  --muted:#7a7a7a;
  --light:#eeeeee;
  --sky:#1e88d6;
  --cyan:#1aa2d8;
  --white:#ffffff;
}
*{box-sizing:border-box;margin:0;padding:0}
html,body{width:1200px;height:3681px;overflow:hidden}
body{position:relative;font-family:'Poppins',sans-serif;color:var(--ink);background:var(--white)}
.abs{position:absolute}

.preview-bar{left:0;top:0;width:1200px;height:103px;background:var(--brand);color:#fff;text-align:center}
.preview-bar .tag{position:absolute;left:0;right:0;top:12px;font-size:21px;text-decoration:underline}
.preview-bar .url{position:absolute;left:0;right:0;top:52px;font-size:23px;padding-left:70px}

.site-header{left:0;top:103px;width:1200px;height:121px;background:#fff}
.brand-mark{left:64px;top:33px;width:74px;height:74px;border-radius:50%;background:var(--brand-dark)}
.brand-name{left:148px;top:38px;color:var(--brand-dark);font-weight:600;line-height:1}
.brand-name .l1{font-size:16px;letter-spacing:1px}
.brand-name .l2{font-size:29px;margin-top:2px}
.brand-name .l3{font-size:11px;margin-top:3px}
.follow{left:744px;top:28px;font-size:10px}
.social-dot{width:27px;height:27px;border-radius:50%;background:var(--royal)}
.call{left:977px;top:17px}
.call small{display:block;font-size:10px}
.call b{font-size:18px;font-weight:500}
.main-nav{left:586px;top:78px;display:flex;gap:21px;font-size:15px;letter-spacing:.5px}

.hero{left:0;top:224px;width:1200px;height:529px;background:linear-gradient(100deg,#1e2a3e 0%,#3a4a61 45%,#2b3850 75%,#1a2436 100%)}
.hero h1{position:absolute;left:64px;top:240px;color:#fff;font-size:32px;font-weight:700}
.hero p{position:absolute;left:64px;top:286px;width:500px;color:#fff;font-size:19px;line-height:1.2}
.btn-hero{position:absolute;left:63px;top:363px;width:170px;height:52px;background:var(--royal);color:#fff;font-size:17px;display:flex;align-items:center;justify-content:center;gap:7px}

.photo{background:linear-gradient(135deg,#8c8a86,#c9c2b8)}
.about-back{left:80px;top:840px;width:253px;height:274px}
.about-front{left:246px;top:923px;width:217px;height:246px;background:linear-gradient(135deg,#9aa3ab,#e0ddd8);box-shadow:0 10px 30px rgba(0,0,0,.15)}
.play{left:227px;top:1014px;width:44px;height:44px;border-radius:50%;background:#fff;border:2px solid #d9d9d9;display:flex;align-items:center;justify-content:center}
.dots{left:66px;top:826px;width:80px;height:80px;background-image:radial-gradient(#c7c7d3 1.5px,transparent 1.6px);background-size:8px 8px}
.about-text{left:501px;top:815px;width:640px}
.about-text h3{color:var(--brand);font-size:22px;font-weight:600}
.about-text h4{font-size:20px;font-weight:600;margin-top:20px}
.about-text p{font-size:15px;line-height:23px;margin-top:14px;color:#333;letter-spacing:.2px}
.btn{position:absolute;height:50px;display:flex;align-items:center;justify-content:center;gap:8px;font-size:16px;font-weight:500}
.btn-fill{left:506px;top:1119px;width:165px;background:var(--brand);color:#fff}
.btn-line{left:690px;top:1119px;width:180px;border:2px solid #ddd;color:var(--ink)}

.services{left:0;top:1251px;width:1200px;height:888px;background:var(--light)}
.services .eyebrow{position:absolute;left:589px;top:45px;font-size:15px}
.services h2{position:absolute;left:501px;top:67px;font-size:28px;font-weight:500}
.service{position:absolute;width:300px}
.service .icon{width:92px;height:92px;border-radius:50%;background:#fff;display:flex;align-items:center;justify-content:center}
.service h3{font-size:20px;font-weight:600;color:var(--navy);margin-top:20px;line-height:25px}
.service p{font-size:15px;line-height:28px;color:var(--muted);margin-top:12px}
.service-card{position:absolute;left:457px;top:146px;width:329px;height:349px;background:#fff}
.service.is-active .icon{background:var(--royal)}

.dedicated h2{position:absolute;left:72px;top:2237px;font-size:22px;font-weight:600;color:#333}
.arrow-btn{top:2244px;width:32px;height:32px;border:1px solid #cfcfcf;display:flex;align-items:center;justify-content:center;background:#fff}
.card{top:2310px;width:252px;height:343px}
.card span{position:absolute;left:20px;bottom:36px;color:#fff;font-size:19px;font-weight:600}

.clients h2{position:absolute;left:0;right:0;top:2718px;text-align:center;font-size:23px;font-weight:600;color:#333}
.clients p{position:absolute;left:220px;width:760px;top:2760px;text-align:center;font-size:15px;line-height:18px}
.logo-row{left:57px;top:2814px;width:1086px;height:107px;display:flex}
.logo-cell{flex:1;display:flex;align-items:center;justify-content:center;border-right:1px solid #ddd;font-size:22px;font-weight:600;color:#333}
.logo-cell:last-child{border-right:none}

.blue-band{left:0;top:3329px;width:1200px;height:352px;background:var(--sky)}
.contact-card{left:56px;top:2997px;width:1088px;height:532px;background:#fff;border:1px solid #e6e6e6;border-radius:6px}
.contact-card h2{position:absolute;left:47px;top:38px;font-size:30px;font-weight:600}
.c-item{position:absolute;left:45px}
.c-icon{width:65px;height:65px;background:#111;display:flex;align-items:center;justify-content:center;border-radius:4px}
.c-text{position:absolute;left:88px;top:-2px;width:320px}
.c-text b{display:block;color:var(--cyan);font-size:23px;font-weight:600}
.c-text span{display:block;font-size:19px;line-height:29px;font-weight:500}
.field-label{position:absolute;font-size:13px;font-weight:500}
.field{position:absolute;border:1px solid #ddd;background:#fff;border-radius:3px}
.select-text{position:absolute;left:20px;top:14px;font-size:13px;color:#777}
.btn-book{position:absolute;left:581px;top:432px;width:154px;height:52px;background:linear-gradient(90deg,#14b6e6,#1a8ad8);color:#fff;font-size:14px;font-weight:600;display:flex;align-items:center;justify-content:center;gap:14px;box-shadow:0 8px 16px rgba(26,138,216,.35)}

.footer-text{left:68px;top:3593px;color:#fff;font-size:15px;font-weight:300}
.footer-text a{color:#fff;text-decoration:none;margin:0 18px}
.foot-dot{top:3585px;width:40px;height:40px;border-radius:50%;background:#e4e4e4}
</style>
</head>
<body>

<div class="abs preview-bar">
  <div class="tag">DEMO</div>
  <div class="url">http://www.studiopreview.net/verrowdale</div>
</div>

<header class="abs site-header">
  <div class="abs brand-mark"></div>
  <div class="abs brand-name">
    <div class="l1">GREATER</div>
    <div class="l2">VERROWDALE</div>
    <div class="l3">CHAMBER OF COMMERCE</div>
  </div>
  <div class="abs follow">FOLLOW</div>
  <div class="abs social-dot" style="left:801px;top:20px" role="img" aria-label="Social profile"></div>
  <div class="abs social-dot" style="left:836px;top:20px" role="img" aria-label="Social profile"></div>
  <div class="abs social-dot" style="left:871px;top:20px;background:#111a3a" role="img" aria-label="Social profile"></div>
  <svg class="abs" style="left:977px;top:22px" width="28" height="28" viewBox="0 0 24 24" fill="none" stroke="#222" stroke-width="1.6"><path d="M5 3h4l2 5-2.5 1.5a11 11 0 0 0 6 6L16 13l5 2v4a2 2 0 0 1-2 2A16 16 0 0 1 3 5a2 2 0 0 1 2-2z"/></svg>
  <div class="abs call" style="left:1012px"><small>CALL US</small><b>555.014.2290</b></div>
  <nav class="abs main-nav"><span>HOME</span><span>ABOUTUS</span><span>SERVICES</span><span>PRODUCTS</span><span>REVIEWS</span><span>KONTAKT</span></nav>
</header>

<section class="abs hero" role="img" aria-label="Photo of colleagues smiling together at a laptop meeting">
  <h1>Build better future together</h1>
  <p>Lorem Ipsum is simply dummy text of the printing and typesetting industry.</p>
  <div class="btn-hero">Learn More
    <svg width="16" height="16" viewBox="0 0 16 16"><circle cx="8" cy="8" r="8" fill="#fff"/><path d="M7 5l3 3-3 3" stroke="#1f49c4" stroke-width="1.8" fill="none"/></svg>
  </div>
</section>

<div class="abs dots"></div>
<div class="abs photo about-back" role="img" aria-label="Photo of a team of women reviewing documents"></div>
<div class="abs about-front" role="img" aria-label="Photo of two colleagues working at a laptop"></div>
<div class="abs play"><svg width="14" height="16" viewBox="0 0 14 16"><path d="M2 1l11 7-11 7z" fill="#1f3f7a"/></svg></div>

<div class="abs about-text">
  <h3>About Us</h3>
  <h4>The story behind our Chamber</h4>
  <p>We denounce with righteous indignation and dislike men beguiled to and de-moralized by the charms of pleasure the moment desire is they they cannot foresee the pain and trouble that are bound ensue and equal blame belongs to those who fail in their duty</p>
  <p>Lorem Ipsum has been the industry's standard dummy text ever since the 1500s, when an unknown printer took a galley of type and scrambled it to make a type specimen book.</p>
</div>
<div class="btn btn-fill">Learn More <svg width="14" height="12" viewBox="0 0 14 12" fill="none" stroke="#fff" stroke-width="1.8"><path d="M1 6h11M8 2l4 4-4 4"/></svg></div>
<div class="btn btn-line">Our Services <svg width="14" height="12" viewBox="0 0 14 12" fill="none" stroke="#222" stroke-width="1.8"><path d="M1 6h11M8 2l4 4-4 4"/></svg></div>

<section class="abs services">
  <div class="eyebrow">What</div>
  <h2>Services We Offer</h2>
  <div class="service-card"></div>

  <div class="service" style="left:134px;top:175px">
    <div class="icon"><svg width="46" height="46" viewBox="0 0 24 24" fill="none" stroke="#1f49c4" stroke-width="1.2"><rect x="3" y="7" width="18" height="13" rx="1"/><path d="M9 7V5h6v2M3 12h18M11 12v2h2v-2"/></svg></div>
    <h3>Company &amp; Business<br>Setup</h3>
    <p>Lorem ipsum dolor sit amet, adipiscing elit. Dui id duis accumsan, eget aliquam varius. A sodales id nulla amet ultricies eget. At nulla mattis mattis.</p>
  </div>
  <div class="service is-active" style="left:486px;top:175px">
    <div class="icon"><svg width="46" height="46" viewBox="0 0 24 24" fill="none" stroke="#fff" stroke-width="1.2"><path d="M4 20h16M6 20v-5h2v5M10 20v-7h2v7M14 20v-9h2v9M5 12l5-4 3 2 6-6M15 4h4v4"/></svg></div>
    <h3>Strategic Consulting</h3>
    <p>Lorem ipsum dolor sit amet, adipiscing elit. Dui id duis accumsan, eget aliquam varius. A sodales id nulla amet ultricies eget. At nulla mattis mattis.</p>
  </div>
  <div class="service" style="left:836px;top:175px">
    <div class="icon"><svg width="46" height="46" viewBox="0 0 24 24" fill="none" stroke="#1f49c4" stroke-width="1.2"><circle cx="12" cy="12" r="5"/><path d="M4 12a8 8 0 0 1 14-5M20 12a8 8 0 0 1-14 5M18 3v4h-4M6 21v-4h4M12 9v6"/></svg></div>
    <h3>Investment Management</h3>
    <p>Lorem ipsum dolor sit amet, adipiscing elit. Dui id duis accumsan, eget aliquam varius. A sodales id nulla amet ultricies eget. At nulla mattis mattis.</p>
  </div>

  <div class="service" style="left:135px;top:530px">
    <div class="icon"><svg width="46" height="46" viewBox="0 0 24 24" fill="none" stroke="#1f49c4" stroke-width="1.2"><rect x="4" y="8" width="10" height="13"/><rect x="14" y="12" width="6" height="9"/><path d="M7 11h4M7 14h4M7 17h4"/><circle cx="18" cy="5" r="2"/></svg></div>
    <h3>Company Management</h3>
    <p>Lorem ipsum dolor sit amet, adipiscing elit. Dui id duis accumsan, eget aliquam varius. A sodales id nulla amet ultricies eget. At nulla mattis mattis.</p>
  </div>
  <div class="service" style="left:486px;top:530px">
    <div class="icon"><svg width="46" height="46" viewBox="0 0 24 24" fill="none" stroke="#1f49c4" stroke-width="1.2"><path d="M9 3h6l-2 4h-2zM11 7C6 10 5 20 12 20s6-10 1-13"/><path d="M14 11h-3a1.5 1.5 0 0 0 0 3h2a1.5 1.5 0 0 1 0 3h-3M12 10v8"/></svg></div>
    <h3>Finance Consulting</h3>
    <p>Lorem ipsum dolor sit amet, adipiscing elit. Dui id duis accumsan, eget aliquam varius. A sodales id nulla amet ultricies eget. At nulla mattis mattis.</p>
  </div>
  <div class="service" style="left:837px;top:530px">
    <div class="icon"><svg width="46" height="46" viewBox="0 0 24 24" fill="none" stroke="#1f49c4" stroke-width="1.2"><circle cx="12" cy="12" r="8"/><circle cx="12" cy="10" r="2.5"/><path d="M8 17c1-3 7-3 8 0M12 2v2M12 20v2M2 12h2M20 12h2"/></svg></div>
    <h3>Human Resources</h3>
    <p>Lorem ipsum dolor sit amet, adipiscing elit. Dui id duis accumsan, eget aliquam varius. A sodales id nulla amet ultricies eget. At nulla mattis mattis.</p>
  </div>
</section>

<section class="dedicated">
  <h2>Dedicated to help anything people’s needs</h2>
  <div class="abs arrow-btn" style="left:1067px"><svg width="10" height="12" viewBox="0 0 10 12" fill="none" stroke="#333" stroke-width="1.5"><path d="M7 1L2 6l5 5"/></svg></div>
  <div class="abs arrow-btn" style="left:1107px"><svg width="10" height="12" viewBox="0 0 10 12" fill="none" stroke="#333" stroke-width="1.5"><path d="M3 1l5 5-5 5"/></svg></div>
  <div class="abs card" style="left:57px;background:linear-gradient(180deg,#8a7a6c,#3f3f45)" role="img" aria-label="Photo of two colleagues at a laptop"><span>Wealth Management</span></div>
  <div class="abs card" style="left:330px;background:linear-gradient(180deg,#b9b9b4,#3b4150)" role="img" aria-label="Photo of a businessman in a suit"><span>Business Planning</span></div>
  <div class="abs card" style="left:607px;background:linear-gradient(180deg,#9a5e44,#55657c)" role="img" aria-label="Photo of a smiling man on the phone with a colleague"><span>Finance Counsulting</span></div>
  <div class="abs card" style="left:887px;background:linear-gradient(180deg,#c2b9ae,#2c3a5a)" role="img" aria-label="Photo of a woman in a meeting"><span>Startup Ideas</span></div>
</section>

<section class="clients">
  <h2>Client we offerd</h2>
  <p>Fürunsere zufriedenen Kunden reinigen wir seit mehr als 15 Jahren Privathäuser, Geschäftsräume, Werkstätten und Praxen in Harmsdorf und Umgebung -und bald auch für Sie?</p>
  <div class="abs logo-row">
    <div class="logo-cell">Harlow Works</div>
    <div class="logo-cell">Brenfield</div>
    <div class="logo-cell">Tessing</div>
    <div class="logo-cell" style="font-size:19px">Dr. Marlo Venn</div>
    <div class="logo-cell">casa-outlet</div>
    <div class="logo-cell">veltrano</div>
  </div>
</section>

<div class="abs blue-band"></div>
<section class="abs contact-card">
  <h2>Contact Us</h2>
  <div class="c-item" style="top:116px">
    <div class="c-icon"><svg width="30" height="30" viewBox="0 0 24 24" fill="#fff"><path d="M5 3h4l2 5-2.5 1.5a11 11 0 0 0 6 6L16 13l5 2v4a2 2 0 0 1-2 2A16 16 0 0 1 3 5a2 2 0 0 1 2-2z"/></svg></div>
    <div class="c-text"><b>Phone</b><span>+49 (0) 155 - 0192 846</span></div>
  </div>
  <div class="c-item" style="top:206px">
    <div class="c-icon"><svg width="34" height="34" viewBox="0 0 24 24" fill="none" stroke="#fff" stroke-width="1.6"><rect x="3" y="5" width="18" height="14" rx="1"/><path d="M3 6l9 7 9-7"/></svg></div>
    <div class="c-text"><b>Email</b><span>info@lindqvist-pflege.de</span></div>
  </div>
  <div class="c-item" style="top:296px">
    <div class="c-icon"><svg width="28" height="32" viewBox="0 0 24 24" fill="#fff"><path d="M12 2a7 7 0 0 0-7 7c0 5 7 13 7 13s7-8 7-13a7 7 0 0 0-7-7zm0 9.5a2.5 2.5 0 1 1 0-5 2.5 2.5 0 0 1 0 5z"/></svg></div>
    <div class="c-text"><b>Address</b><span>Lindqvist Pflege &amp; Service</span><span>Almenweg 12</span><span>78290 Harmsdorf</span></div>
  </div>

  <div class="field-label" style="left:581px;top:80px">Name</div>
  <div class="field" style="left:581px;top:110px;width:217px;height:44px"></div>
  <div class="field-label" style="left:824px;top:80px">Email</div>
  <div class="field" style="left:824px;top:110px;width:219px;height:44px"></div>
  <div class="field-label" style="left:581px;top:172px">Phone</div>
  <div class="field" style="left:581px;top:206px;width:217px;height:44px"></div>
  <div class="field-label" style="left:824px;top:172px">Services</div>
  <div class="field" style="left:824px;top:206px;width:219px;height:44px"><span class="select-text">Choose services</span>
    <svg style="position:absolute;right:20px;top:18px" width="10" height="6" viewBox="0 0 10 6" fill="none" stroke="#777" stroke-width="1.3"><path d="M1 1l4 4 4-4"/></svg></div>
  <div class="field-label" style="left:581px;top:268px">Message</div>
  <div class="field" style="left:581px;top:303px;width:462px;height:90px"></div>
  <div class="btn-book">Book Now <svg width="12" height="12" viewBox="0 0 12 12" fill="none" stroke="#fff" stroke-width="1.6"><path d="M2 10L10 2M4 2h6v6"/></svg></div>
</section>

<div class="abs footer-text">Greater Verrowdale © 2022 All Rights Reserved | <a>Terms &amp; Condition</a>| <a>Privacy Policy</a></div>
<div class="abs foot-dot" style="left:997px" role="img" aria-label="Social profile"></div>
<div class="abs foot-dot" style="left:1047px" role="img" aria-label="Social profile"></div>
<div class="abs foot-dot" style="left:1097px" role="img" aria-label="Social profile"></div>

</body>
</html>
```